I need a business card design for a new company that will be doing consulting work around issues of cultural competency, and diversity and inclusion. I would like the design to be crisp and clear with bold but conservative colors and incorporate shades of blue

Target Market(s)

Small businesses, schools, non-profits

Industry/Entity Type

Consulting

Font styles to use
Serif
Sans Serif

Colors
0c5ba6
6b449b
3276b5
0292cd

Requirements
Must have
• A Morrow Venture (name of company)
• Lemlem Tavish
• CEO
• lemlem@amorrowventure.com
• (215)483-2756

```html
<!DOCTYPE html>
<html lang="en">
<head>
<meta charset="utf-8">
<title>A Morrow Venture — Business Card</title>
<link href="https://fonts.googleapis.com/css2?family=Montserrat:wght@600;700&family=Lexend:wght@400&display=swap" rel="stylesheet">
<style>
  :root {
    --brand-blue: #125da8;
    --ink: #1c1c1c;
    --paper: #ffffff;
    --edge: #e2e2e2;
  }
  html, body {
    margin: 0;
    padding: 0;
    width: 1200px;
    height: 1200px;
    overflow: hidden;
    background: var(--paper);
  }
  .canvas {
    position: relative;
    width: 1200px;
    height: 1200px;
  }
  .card {
    position: absolute;
    left: 232px;
    top: 389px;
    width: 738px;
    height: 421px;
    border-radius: 36px;
    background: var(--paper);
    box-shadow: 0 0 0 3px var(--edge);
    overflow: hidden;
  }
  .header-band {
    position: absolute;
    left: 0;
    top: 0;
    width: 100%;
    height: 112px;
    background: var(--brand-blue);
    display: flex;
    align-items: center;
    justify-content: center;
  }
  .company-name {
    margin: 0;
    font-family: "Montserrat", sans-serif;
    font-weight: 600;
    font-size: 43px;
    letter-spacing: 0.5px;
    color: var(--paper);
    text-transform: uppercase;
  }
  .band-pointer {
    position: absolute;
    left: 191px;
    top: 111px;
  }
  .person {
    position: absolute;
    left: 203px;
    top: 240px;
    transform: translateX(-50%);
    text-align: center;
  }
  .person-name {
    margin: 0;
    font-family: "Montserrat", sans-serif;
    font-weight: 700;
    font-size: 27px;
    line-height: 36px;
    color: var(--brand-blue);
    text-transform: uppercase;
    white-space: nowrap;
  }
  .person-title {
    margin: 0 auto;
    width: 74px;
    font-family: "Lexend", sans-serif;
    font-size: 17px;
    line-height: 20px;
    color: var(--ink);
    padding-bottom: 2px;
    border-bottom: 2px solid var(--brand-blue);
  }
  .contact {
    position: absolute;
    left: 526px;
    transform: translateX(-50%);
    display: flex;
    flex-direction: column;
    align-items: center;
  }
  .contact-phone { top: 116px; }
  .contact-email { top: 199px; }
  .contact-icon {
    width: 36px;
    height: 36px;
    display: block;
  }
  .contact-text {
    margin-top: 10px;
    font-family: "Lexend", sans-serif;
    font-size: 18px;
    letter-spacing: 1px;
    color: var(--ink);
    white-space: nowrap;
  }
  .contact-text a { color: inherit; text-decoration: none; }
</style>
</head>
<body>
<div class="canvas">
  <article class="card">
    <header class="header-band">
      <h1 class="company-name">A Morrow Venture</h1>
    </header>
    <svg class="band-pointer" width="28" height="27" viewBox="0 0 28 27" aria-hidden="true">
      <polygon points="0,0 28,0 0,26" fill="var(--brand-blue)"/>
    </svg>

    <div class="person">
      <p class="person-name">Lemlem Tavish</p>
      <p class="person-title">CEO</p>
    </div>

    <div class="contact contact-phone">
      <svg class="contact-icon" viewBox="0 0 36 36" aria-hidden="true">
        <circle cx="18" cy="18" r="18" fill="var(--brand-blue)"/>
        <path d="M12.5 10.5c.6-.6 1.5-.6 2 0l2 2.3c.5.5.5 1.3 0 1.8l-1.2 1.2c.9 1.9 2.4 3.4 4.3 4.3l1.2-1.2c.5-.5 1.3-.5 1.8 0l2.3 2c.6.5.6 1.4 0 2l-1.3 1.3c-.8.8-2 1-3 .6-4.3-1.6-7.7-5-9.3-9.3-.4-1-.2-2.2.6-3z" fill="var(--paper)"/>
        <path d="M20 10.5a5.5 5.5 0 0 1 5.5 5.5M20 13.3a2.7 2.7 0 0 1 2.7 2.7" stroke="var(--paper)" stroke-width="1.4" fill="none" stroke-linecap="round"/>
      </svg>
      <span class="contact-text"><a href="tel:+12154832756">(215)483-2756</a></span>
    </div>

    <div class="contact contact-email">
      <svg class="contact-icon" viewBox="0 0 36 36" aria-hidden="true">
        <circle cx="18" cy="18" r="18" fill="var(--brand-blue)"/>
        <rect x="10.5" y="12.5" width="15" height="11" rx="1" fill="var(--paper)"/>
        <path d="M10.5 13l7.5 6 7.5-6" stroke="var(--brand-blue)" stroke-width="1.4" fill="none"/>
      </svg>
      <span class="contact-text"><a href="mailto:lemlem@amorrowventure.com">lemlem@amorrowventure.com</a></span>
    </div>
  </article>
</div>
</body>
</html>
```